Brochure Design For Beauty Salon

We have an existing brochure for our beauty salon business which has been designed in-house.

We need a designer to refresh the look and feel of the brochure, which is intended for print. The print format will be 210mmx210mm (square, stapled).

We need a design for each and every page of the brochure, including the front and back covers.

We are looking for a fresh modern design, quite close to what we already have, but looking more slick and professional.

The primary colors are white, grey and purple. The final design will communicate luxury, prestige and cleanliness and have a heavy focus on creating the feeling of space within each page.

Target Market(s)

Professional Women, aged 20-45

Industry/Entity Type

Beauty Salon

Font styles to use
Sans Serif
Other font styles liked:
• Helvetica

Requirements
Must have
• The project must be ready for print on square paper 210x210mm

```html
<!DOCTYPE html>
<html lang="en">
<head>
<meta charset="utf-8">
<title>Vera Lumi Treatment Brochure</title>
<link href="https://fonts.googleapis.com/css2?family=Montserrat:wght@500;600;700;800;900&family=Lato:ital,wght@0,400;0,700;1,400&display=swap" rel="stylesheet">
<style>
:root{
  --plum:#5b0b31;
  --plum-light:#7d3058;
  --paper:#ffffff;
  --paper-grey:#ececec;
  --frame-grey:#d9d9d9;
  --ink:#3c3c3c;
  --muted:#8a8a8a;
  --rule:#c9c9c9;
  --backdrop:#e6e6e6;
}
*{box-sizing:border-box;margin:0;padding:0}
html,body{width:901px;height:1200px;overflow:hidden;background:var(--backdrop)}
body{position:relative;font-family:"Lato",Helvetica,Arial,sans-serif;color:var(--ink)}
.spread{position:absolute;left:54px;width:808px;height:416px;box-shadow:0 6px 16px rgba(0,0,0,.18)}
.spread--facials{top:80px}
.spread--massage{top:680px}
.page{position:absolute;top:0;width:404px;height:416px;overflow:hidden}
.page--left{left:0}
.page--right{left:404px}
.plum-bg{background:linear-gradient(120deg,var(--plum) 0%,var(--plum) 55%,var(--plum-light) 100%)}
.abs{position:absolute}
.photo{position:absolute;border:4px solid var(--paper);box-shadow:0 1px 3px rgba(0,0,0,.2)}
.photo--skin{background:linear-gradient(135deg,#f1e1d6,#d9b7a3)}
.photo--room{background:linear-gradient(135deg,#4a3a3c,#c9a693)}
.photo--stone{background:linear-gradient(135deg,#e2cbbd,#3a2e2c)}
.heading{font-family:"Montserrat",Helvetica,sans-serif;font-weight:700;font-size:10.5px;letter-spacing:1.3px;color:var(--plum);text-transform:uppercase;white-space:nowrap}
.heading--light{color:var(--paper)}
.bar{position:absolute;width:30px;height:3px;background:var(--plum)}
.bar--light{background:var(--paper)}
.intro{font-size:7.5px;line-height:1.5;color:#777}
.intro--light{color:#f1dbe5}
.row{position:absolute;display:flex;justify-content:space-between;align-items:flex-end;font-family:"Montserrat",Helvetica,sans-serif;font-size:6.3px;font-weight:600;letter-spacing:.6px;color:var(--ink);border-bottom:1px solid var(--rule);padding-bottom:2px;white-space:nowrap}
.row .price{color:var(--muted);font-weight:500;border-bottom:2px solid var(--plum);margin-bottom:-3px;padding-bottom:1px}
.row--light{color:var(--paper);border-bottom-color:rgba(255,255,255,.55)}
.row--light .price{color:var(--paper);border-bottom-color:var(--paper)}
.note{position:absolute;font-style:italic;font-size:6px;line-height:1.55;color:var(--muted)}
.note--light{color:#e9cad8}
.display{font-family:"Montserrat",Helvetica,sans-serif;font-weight:900;font-size:22px;letter-spacing:1.5px;color:var(--plum)}
.body-copy{font-size:7px;line-height:1.7;color:var(--muted)}
.button{position:absolute;border:1.5px solid var(--paper);color:var(--paper);font-family:"Montserrat",Helvetica,sans-serif;font-weight:800;font-size:7.5px;letter-spacing:1.8px;display:flex;align-items:center;justify-content:center}
</style>
</head>
<body>

<section class="spread spread--facials">
  <div class="page page--left plum-bg">
    <div class="abs" style="left:76px;top:16px;width:318px;height:384px;background:var(--paper)"></div>
    <div class="photo photo--skin" role="img" aria-label="Photo of a woman receiving a facial massage" style="left:19px;top:60px;width:90px;height:92px"></div>
    <div class="photo photo--skin" role="img" aria-label="Photo of a gloved hand treating a woman's eye area" style="left:19px;top:238px;width:90px;height:88px"></div>

    <h2 class="heading abs" style="left:130px;top:66px">Signature Facials</h2>
    <div class="bar" style="left:130px;top:84px"></div>
    <p class="intro abs" style="left:130px;top:98px;width:250px">Deep cleansing and ultra hydrating, our signature facials are tailor made for your skin.</p>
    <div class="row" style="left:130px;top:128px;width:251px"><span>Express Focus Signature Facial</span><span class="price">£35 | 30 mins</span></div>
    <p class="note" style="left:130px;top:146px;width:250px">We focus on key stages of treatment to get you maximum results in a minimum of time.</p>
    <div class="row" style="left:130px;top:164px;width:251px"><span>Vera Lumi Signature Facial</span><span class="price">£55 | 60 mins</span></div>
    <p class="note" style="left:130px;top:181px;width:250px">A bespoke facial customised at every stage.</p>
    <div class="row" style="left:130px;top:200px;width:251px"><span>Luxury Signature Facial</span><span class="price">£85 | 90 mins</span></div>
    <p class="note" style="left:130px;top:216px;width:250px">Upgrade to the luxury facial and enjoy a deeply hydrating masque and soothing touch therapy</p>

    <h2 class="heading abs" style="left:130px;top:249px">Eye Lift</h2>
    <div class="bar" style="left:130px;top:266px"></div>
    <div class="row" style="left:130px;top:278px;width:251px"><span>Eyelift Express Facial</span><span class="price">£35 | 30 mins</span></div>
    <p class="note" style="left:130px;top:296px;width:250px">This intensive, energising professional treatment focuses on the eye area and delivers benefits including lymph drainage, reduced puffiness, fewer visible fine lines and brighter skin around the eyes</p>
    <div class="row" style="left:130px;top:343px;width:251px"><span>Eyelift Add-on</span><span class="price">£15 | 15 mins</span></div>
    <p class="note" style="left:130px;top:360px;width:250px">This eye-opening service is to illuminate the eye area and promote an energised, positive appearance while the body is experiencing stress. It delivers quick, visible eye benefits. Add this 15 minute service to your regular facial</p>
  </div>

  <div class="page page--right" style="background:var(--paper-grey)">
    <div class="abs plum-bg" style="left:0;top:0;width:404px;height:19px"></div>
    <div class="abs plum-bg" style="left:386px;top:0;width:18px;height:394px"></div>
    <div class="abs photo--skin" role="img" aria-label="Photo of a relaxed woman receiving a facial with hands on her temples" style="left:12px;top:19px;width:374px;height:213px"></div>
    <div class="abs plum-bg" style="left:15px;top:232px;width:371px;height:162px"></div>
    <h2 class="heading heading--light abs" style="left:102px;top:248px">Teenage Facials</h2>
    <div class="bar bar--light" style="left:102px;top:265px"></div>
    <p class="intro intro--light abs" style="left:102px;top:278px;width:270px">Fresh Start from Solenne is a skincare range specialising in teen skin</p>
    <div class="row row--light" style="left:102px;top:300px;width:263px"><span>Fresh Start Express Facial</span><span class="price">£30 | 30 mins</span></div>
    <p class="note note--light" style="left:102px;top:316px;width:263px">We focus on key stages of treatment to get you maximum results in a minimum of time.</p>
    <div class="row row--light" style="left:102px;top:337px;width:263px"><span>Fresh Start Signature Facial</span><span class="price">£48 | 60 mins</span></div>
    <div class="row row--light" style="left:102px;top:363px;width:263px"><span>Fresh Start Luxury Facial</span><span class="price">£75 | 90 mins</span></div>
  </div>
</section>

<section class="spread spread--massage">
  <div class="page page--left" style="background:var(--frame-grey)">
    <div class="abs plum-bg" style="left:0;top:136px;width:26px;height:280px"></div>
    <div class="abs plum-bg" style="left:0;top:398px;width:404px;height:18px"></div>
    <div class="abs" style="left:26px;top:16px;width:362px;height:382px;background:var(--paper)"></div>
    <div class="abs plum-bg" style="left:26px;top:136px;width:40px;height:124px"></div>
    <h1 class="display abs" style="left:122px;top:62px">MASSAGE</h1>
    <div class="abs" style="left:122px;top:95px;width:74px;height:3px;background:#777"></div>
    <div class="abs photo--room" role="img" aria-label="Photo of a therapist massaging a client's back" style="left:66px;top:136px;width:164px;height:124px"></div>
    <div class="body-copy abs" style="left:250px;top:134px;width:134px">
      <p>You need a massage that combines the best techniques from around the world, using the finest oils and experienced, expert hands to leave you feeling brand new again. You need a Vera Lumi Signature massage.</p>
      <p style="margin-top:8px">Choose your ideal massage from our menu below. Each massage will be tailored to your needs which will be discussed before your treatment begins.</p>
    </div>
    <h2 class="heading abs" style="left:122px;top:290px">Vera Lumi Signature Massage</h2>
    <div class="bar" style="left:122px;top:307px"></div>
    <div class="row" style="left:122px;top:318px;width:258px"><span>Signature Back, Neck and Shoulders</span><span class="price">30 mins | £32.00</span></div>
    <div class="row" style="left:122px;top:344px;width:258px"><span>Signature Full Body</span><span class="price">60 mins | £49.00</span></div>
    <div class="row" style="left:122px;top:370px;width:258px"><span>Signature Luxury Massage</span><span class="price">90 mins | £72.00</span></div>
  </div>

  <div class="page page--right" style="background:var(--paper-grey)">
    <div class="abs plum-bg" style="left:0;top:0;width:404px;height:14px"></div>
    <div class="abs plum-bg" style="left:386px;top:0;width:18px;height:392px"></div>
    <div class="abs" style="left:15px;top:14px;width:371px;height:242px;background:var(--frame-grey)"></div>
    <div class="abs" style="left:95px;top:70px;width:291px;height:186px;background:var(--paper)"></div>
    <div class="photo photo--room" role="img" aria-label="Photo of a therapist at a massage table" style="left:25px;top:28px;width:54px;height:80px"></div>
    <div class="photo photo--skin" role="img" aria-label="Photo of a couple receiving massages" style="left:102px;top:28px;width:78px;height:48px"></div>
    <div class="photo photo--stone" role="img" aria-label="Photo of hands massaging a back with oil" style="left:192px;top:28px;width:78px;height:48px"></div>
    <div class="photo photo--skin" role="img" aria-label="Photo of a woman relaxing during a shoulder massage" style="left:284px;top:28px;width:78px;height:48px"></div>

    <h2 class="heading abs" style="left:100px;top:96px">Contemporary Massage</h2>
    <div class="bar" style="left:100px;top:113px"></div>
    <p class="intro abs" style="left:100px;top:126px;width:270px">Deep cleansing and ultra hydrating, our signature facials are tailor made for your skin.</p>
    <div class="row" style="left:100px;top:166px;width:266px"><span>Indian Head Massage</span><span class="price">£45 | 45 mins</span></div>
    <div class="row" style="left:100px;top:194px;width:266px"><span>Solenne Mud massage</span><span class="price">£60 | 60 mins</span></div>
    <div class="row" style="left:100px;top:221px;width:266px"><span>Thermal Compress massage</span><span class="price">£65 | 60 mins</span></div>

    <div class="abs plum-bg" style="left:15px;top:256px;width:371px;height:136px"></div>
    <div class="photo photo--stone" role="img" aria-label="Photo of a woman receiving a warm stone massage" style="left:18px;top:228px;width:68px;height:60px"></div>
    <h2 class="heading heading--light abs" style="left:100px;top:265px">Ember Shells Massage</h2>
    <div class="bar bar--light" style="left:100px;top:282px"></div>
    <div class="row row--light" style="left:100px;top:294px;width:266px"><span>Ember Shells Back Massage</span><span class="price">£38 | 30 mins</span></div>
    <div class="row row--light" style="left:100px;top:322px;width:266px"><span>Ember Shells Full Body Massage</span><span class="price">£65 | 60 min</span></div>
    <div class="button" style="left:178px;top:356px;width:112px;height:23px">COMING SOON!</div>
  </div>
</section>

</body>
</html>
```